webdesign for a spectacles/glasses designer

Hello,

Someone in my village designs his own spectacles/eyeglasses.

For this I need a design that looks better than my poor design skills ;o)

The site is based around collections, subcollections and the actual items.

So we need a design that lists these in a nice way, worst case on seperate pages.

Here you can find the working material...

https://www.filevaultic.com/s/q7kmtr4p2wz91xb/BriefHarbor.zip

keep an eye on the product_tree file.

first level is the collection name
2nd is the model group
3rd is the model (on most of them it's just a different color of the same base model)

I added a seperate contact info file (line is too slow to reupload 60Mb again :( )

https://dl.filevaulticcontent.com/u/31906524/Anselm/contact.zip

I think I forgot to mention that it will be a shop like site to present his products,
altho I will add a cart system there won't be a payment system linked to it as
people who place orders will get contacted with payment instructions.
Updates

In the zipfile /Logo/logo_mistral_font.psd is the main logo
(you need to change character spacing to 1 to get rid of the spacing gaps)

the other one is only a collection logo

Target Market(s)

Plain customers and his resellers.

Industry/Entity Type

Shop

Requirements
Must have
• - a design that suits responsive behaviour (via the 960 grid)
- a menu is always handy (home, about, collections, contact)
- highlighted area/slider to highlight his sunglasses over glasses thingy
- featured products (newly added or promotional stuff)

there is a lot of pretty pictures to be supplied so do what you think is best

Nice to have
• a roll over zoom with selectable thumbnails or a plain gallery with full picture display at the product page.

maybe a drop down menu for the collection part (I will supply a screenshot of the backend structure)

```html
<!DOCTYPE html>
<html lang="en">
<head>
<meta charset="utf-8">
<title>Anselm Eyewear – Shop</title>
<link rel="stylesheet" href="https://fonts.googleapis.com/css2?family=Arimo:wght@400;700&family=Arvo:wght@400;700&display=swap">
<style>
:root{
  --page:#1d2021;
  --white:#ffffff;
  --salmon:#f47c65;
  --salmon-line:#f3a593;
  --ink:#2b2725;
  --hero:#4d4846;
  --panel-dark:#3b3634;
  --toolbar:#161616;
  --line:#e3e3e3;
  --footer-dark:#161b1d;
  --footer-link:#e0453a;
  --footer-rule:#4d7787;
}
*{box-sizing:border-box;margin:0;padding:0}
html,body{width:1200px;height:1000px;overflow:hidden;background:var(--page);font-family:"Arimo",Arial,sans-serif;color:var(--ink)}
.canvas{position:relative;width:1200px;height:1000px;background:radial-gradient(ellipse at 85% 20%,#2b3436 0%,var(--page) 55%)}
.abs{position:absolute}
h1,h2,h3,h4{font-weight:400}

/* header */
.site-header{left:230px;top:0;width:718px;height:80px;background:var(--white)}
.brand{left:6px;top:8px;display:flex;align-items:center;gap:6px}
.brand-mark{width:14px;height:14px;border-radius:50%;background:var(--ink)}
.brand-name{font-size:26px;font-weight:700;color:var(--ink);letter-spacing:1px}
.brand-sub{left:4px;top:66px;font-size:9px;color:var(--ink)}
.main-nav{left:254px;top:15px;display:flex;gap:26px;font-size:13px;color:#222}
.main-nav span small{font-size:8px;margin-left:2px}
.social{left:642px;top:17px;display:flex;gap:8px}
.social i{display:block;width:10px;height:10px;border-radius:50%;background:#777}
.salmon-band{left:230px;top:80px;width:718px;height:7px;background:var(--salmon)}
.toolbar{left:230px;top:87px;width:718px;height:17px;background:var(--toolbar);color:#fff;font-size:7.5px;font-weight:700}
.toolbar span{position:absolute;top:5px}
.search-icon{position:absolute;left:112px;top:4px}

/* hero */
.hero{left:230px;top:104px;width:718px;height:226px;background:var(--hero)}
.hero h1{position:absolute;left:23px;top:34px;font-size:24px;color:#fff;letter-spacing:.5px}
.hero p{position:absolute;left:23px;top:67px;font-size:12px;line-height:13px;color:#fff;letter-spacing:.3px}
.hero-photo{position:absolute;left:379px;top:0;width:339px;height:226px;
  background:
    radial-gradient(ellipse 60px 75px at 105px 70px,rgba(214,190,140,.9),rgba(214,190,140,0) 100%),
    radial-gradient(ellipse 40px 45px at 118px 112px,rgba(205,160,130,.85),rgba(205,160,130,0) 100%),
    radial-gradient(ellipse 45px 55px at 268px 110px,rgba(200,150,125,.7),rgba(200,150,125,0) 100%),
    radial-gradient(ellipse 95px 55px at 140px 215px,rgba(25,22,20,.95),rgba(25,22,20,0) 100%),
    radial-gradient(ellipse 45px 30px at 175px 205px,rgba(190,160,50,.75),rgba(190,160,50,0) 100%),
    linear-gradient(100deg,#6a6462 0%,#7a7572 50%,#6b6664 100%)}
.btn{display:inline-block;background:var(--salmon);color:#fff;font-size:11px;letter-spacing:.4px}
.hero .btn{position:absolute;left:23px;top:132px;padding:6px 5px;font-size:12px}

/* featured */
.featured{left:230px;top:330px;width:718px;height:144px;background:linear-gradient(#fff,#f7f7f7)}
.section-title{font-family:"Arvo",Georgia,serif;color:#333;font-weight:400}
.featured .section-title{position:absolute;left:12px;top:6px;font-size:12.5px}
.featured-row{position:absolute;left:0;top:27px;display:flex}
.feat-item{width:90px;height:117px;border-right:1px solid var(--line);position:relative;background:#fff}
.frame-photo{background:
    radial-gradient(ellipse 38% 9% at 50% 50%,var(--tone),rgba(255,255,255,0) 100%),
    radial-gradient(ellipse 22% 16% at 28% 50%,rgba(255,255,255,.7),rgba(255,255,255,0) 100%),
    linear-gradient(#f3f3f3,#e6e6e6)}
.feat-photo{position:absolute;left:0;top:0;width:89px;height:90px}
.feat-item .btn{position:absolute;left:14px;top:94px;padding:4px 4px;font-size:9.5px}
.arrow{position:absolute;top:61px;width:24px;height:24px;border-radius:50%;background:#2a2a2a}
.arrow svg{display:block;margin:7px auto}

/* columns */
.col-left{left:230px;top:474px;width:143px;height:359px;background:#fff}
.col-center{left:374px;top:474px;width:429px;height:359px;background:#fff}
.col-right{left:804px;top:474px;width:144px;height:359px;background:#fff}
.side-title{font-size:11.5px;color:#222;letter-spacing:.3px}
.cat-list{position:absolute;left:10px;top:35px;width:122px;list-style:none}
.cat-list li{position:relative;height:23px;border-top:1px solid var(--salmon-line);font-size:12px;padding:4px 4px}
.cat-list li:last-child{border-bottom:1px solid var(--salmon-line)}
.plus{position:absolute;right:4px;top:6px;width:11px;height:11px;border-radius:50%;background:#3a3a3a}
.plus::before,.plus::after{content:"";position:absolute;background:#fff;left:3px;top:5px;width:5px;height:1px}
.plus::after{left:5px;top:3px;width:1px;height:5px}
.promo{position:absolute;left:0;width:143px;height:95px;background:var(--panel-dark);color:#fff}
.promo h3{position:absolute;left:14px;top:7px;font-size:18px;letter-spacing:.6px}
.promo p{position:absolute;left:14px;top:35px;font-size:8.5px;line-height:10px;width:92px}

.article-title{position:absolute;left:12px;top:9px;font-size:15px;color:#3a2a28;letter-spacing:.4px}
.article-photo{position:absolute;left:11px;top:34px;width:160px;height:158px;background:
    radial-gradient(ellipse 110px 40px at 40px 40px,rgba(60,35,25,.95),rgba(60,35,25,0) 100%),
    radial-gradient(ellipse 30px 110px at 15px 110px,rgba(70,42,30,.85),rgba(70,42,30,0) 100%),
    linear-gradient(135deg,#f6f5f3,#ecebe8 60%,#e2e0dd)}
.article-text{position:absolute;left:185px;top:46px;width:190px;font-size:7.6px;line-height:10.6px;color:#111;letter-spacing:.3px}
.col-center .article-btn{position:absolute;left:185px;top:160px;padding:4px 5px;font-size:10px}
.latest-head{position:absolute;left:11px;top:195px;width:406px;height:26px;border-bottom:1px solid var(--salmon-line)}
.latest-head .section-title{font-size:16.5px;color:#222}
.switch-view{position:absolute;right:12px;top:7px;font-size:7px;color:#444;display:flex;align-items:center;gap:3px}
.switch-view i{display:block;width:9px;height:7px;border:1px solid #888;background:#ddd}
.latest-note{position:absolute;left:12px;top:234px;font-size:7.5px;color:#333}
.latest-row{position:absolute;left:8px;top:262px;display:flex;gap:13px}
.latest-tile{width:94px;height:97px;border:1px solid #ddd;border-bottom:2px solid var(--salmon);background:#fff;padding:3px}
.latest-photo{width:86px;height:85px;--tone:rgba(140,120,200,.55)}

.side-box{position:absolute;left:0;width:144px;border-bottom:1px solid #ddd}
.side-box .side-title{position:absolute;left:13px;top:13px;font-size:12px}
.side-box p{position:absolute;left:12px;top:36px;font-size:6.5px;line-height:8.5px;color:#555;width:118px}
.contact-link{position:absolute;left:13px;top:36px;width:118px;font-size:9.5px;font-weight:700;color:#333;border-top:1px solid var(--salmon-line);border-bottom:1px solid var(--salmon-line);padding:4px 1px 6px}
.pay-badge{position:absolute;left:27px;top:316px;width:89px;height:35px;border-radius:5px;background:linear-gradient(#fff3c8,#f3d47a);border:1px solid #d9b35a}

/* footers */
.footer-links{left:230px;top:835px;width:484px;height:85px;background:var(--footer-dark);display:flex;gap:23px;padding:8px 0 8px 19px}
.footer-col{width:138px;flex:none}
.footer-col h4{font-size:11px;color:#fff;padding-bottom:6px;border-bottom:1px solid var(--footer-rule);margin-bottom:10px}
.footer-col li{list-style:none;font-size:7.5px;font-weight:700;color:var(--footer-link);line-height:12.5px}
.bottom-bar{left:230px;top:936px;width:722px;height:64px;background:#fff}
.bottom-nav{position:absolute;left:0;right:0;top:12px;text-align:center;font-family:"Arvo",Georgia,serif;font-size:9.5px;color:#333}
.to-top{position:absolute;left:690px;top:37px;width:20px;height:20px;border-radius:4px;background:#e85a55}
.to-top svg{display:block;margin:6px auto}
</style>
</head>
<body>
<div class="canvas">

  <header class="abs site-header">
    <div class="abs brand"><span class="brand-mark"></span><span class="brand-name">AC</span></div>
    <div class="abs brand-sub">By Anselm</div>
    <nav class="abs main-nav">
      <span>Home</span><span>About<small>&#9662;</small></span><span>Collections<small>&#9662;</small></span><span>Contact</span>
    </nav>
    <div class="abs social"><i></i><i></i><i></i></div>
  </header>
  <div class="abs salmon-band"></div>
  <div class="abs toolbar">
    <span style="left:7px">Search...</span>
    <svg class="search-icon" width="8" height="8" viewBox="0 0 8 8"><circle cx="3.2" cy="3.2" r="2.3" fill="none" stroke="#fff" stroke-width="1.2"/><path d="M5 5l2.5 2.5" stroke="#fff" stroke-width="1.3"/></svg>
    <span style="left:128px">Default welcome msg!</span>
    <span style="left:460px">Cart (0 items)</span>
    <span style="left:521px">Log In</span>
    <span style="left:559px">Sign Up</span>
    <span style="left:604px">Text Size &nbsp;A &nbsp;<b style="font-size:10px">A</b></span>
  </div>

  <section class="abs hero">
    <h1>AMAZING HEADING</h1>
    <p>Lorem &nbsp;Ipsum and some very great words would go here<br>It would have a great impact on your site.<br>Users will flock and buy!</p>
    <span class="btn">Read More</span>
    <div class="hero-photo" role="img" aria-label="Photo of a blonde woman in dark-framed glasses holding up two more frames"></div>
  </section>

  <section class="abs featured">
    <h2 class="section-title">Featured Products</h2>
    <div class="featured-row">
      <div class="feat-item"><div class="feat-photo frame-photo" style="--tone:rgba(180,70,90,.5)" role="img" aria-label="Red metal eyeglass frame"></div><span class="btn">Read More</span></div>
      <div class="feat-item"><div class="feat-photo frame-photo" style="--tone:rgba(190,120,80,.5)" role="img" aria-label="Copper metal eyeglass frame"></div><span class="btn">Read More</span></div>
      <div class="feat-item"><div class="feat-photo frame-photo" style="--tone:rgba(140,120,200,.5)" role="img" aria-label="Lilac metal eyeglass frame"></div><span class="btn">Read More</span></div>
      <div class="feat-item"><div class="feat-photo frame-photo" style="--tone:rgba(150,110,90,.5)" role="img" aria-label="Bronze metal eyeglass frame"></div><span class="btn">Read More</span></div>
      <div class="feat-item"><div class="feat-photo frame-photo" style="--tone:rgba(200,100,60,.5)" role="img" aria-label="Orange metal eyeglass frame"></div><span class="btn">Read More</span></div>
      <div class="feat-item"><div class="feat-photo frame-photo" style="--tone:rgba(110,110,115,.5)" role="img" aria-label="Grey metal eyeglass frame"></div><span class="btn">Read More</span></div>
      <div class="feat-item"><div class="feat-photo frame-photo" style="--tone:rgba(130,130,135,.45)" role="img" aria-label="Silver metal eyeglass frame"></div><span class="btn">Read More</span></div>
      <div class="feat-item"><div class="feat-photo frame-photo" style="--tone:rgba(150,150,155,.4)" role="img" aria-label="Light silver eyeglass frame"></div><span class="btn">Read More</span></div>
    </div>
    <div class="arrow" style="left:2px"><svg width="10" height="10" viewBox="0 0 10 10"><path d="M6.5 1.5L3 5l3.5 3.5" fill="none" stroke="#fff" stroke-width="1.6"/></svg></div>
    <div class="arrow" style="left:692px"><svg width="10" height="10" viewBox="0 0 10 10"><path d="M3.5 1.5L7 5 3.5 8.5" fill="none" stroke="#fff" stroke-width="1.6"/></svg></div>
  </section>

  <aside class="abs col-left">
    <h3 class="side-title" style="position:absolute;left:13px;top:13px">Product Categories</h3>
    <ul class="cat-list">
      <li>Lorem<span class="plus"></span></li>
      <li>Ipsum<span class="plus"></span></li>
      <li>Another<span class="plus"></span></li>
    </ul>
    <div class="promo" style="top:118px"><h3>Lorem</h3><p>Lorem Ipsum any text can go here.<br>Or. This can go all-together.</p></div>
  </aside>

  <main class="abs col-center">
    <h2 class="article-title">A Big Long Title of Meaning Can Go Here</h2>
    <div class="article-photo" role="img" aria-label="Close-up of tortoiseshell eyeglass frame"></div>
    <p class="article-text">Lorem Ipsum is simply dummy text of the printing and typesetting industry. Lorem Ipsum has been the industry's standard dummy text ever since the 1500s, when an unknown printer took a galley of type and scrambled it to make a type specimen book. It has survived not only five centuries, but also the leap into electronic typesetting, remaining essentially unchanged. It was popularised in the 1960s with the release of Typeleaf sheets containing Lorem Ipsum passages, and more recently.</p>
    <span class="btn article-btn">Read More</span>
    <div class="latest-head">
      <h2 class="section-title">Latest products</h2>
      <div class="switch-view"><i></i><i></i>&nbsp;Switch View</div>
    </div>
    <p class="latest-note">Check out a selection of our items currently for sale:</p>
    <div class="latest-row">
      <div class="latest-tile"><div class="latest-photo frame-photo" role="img" aria-label="Purple metal eyeglass frame"></div></div>
      <div class="latest-tile"><div class="latest-photo frame-photo" role="img" aria-label="Purple metal eyeglass frame"></div></div>
      <div class="latest-tile"><div class="latest-photo frame-photo" role="img" aria-label="Purple metal eyeglass frame"></div></div>
      <div class="latest-tile"><div class="latest-photo frame-photo" role="img" aria-label="Purple metal eyeglass frame"></div></div>
    </div>
  </main>

  <aside class="abs col-right">
    <div class="side-box" style="top:0;height:63px"><h3 class="side-title">Compare Products</h3><p>You have no items to compare.</p></div>
    <div class="side-box" style="top:63px;height:74px"><h3 class="side-title" style="top:14px">My Cart</h3><p style="top:36px">You have no items in your shopping cart.</p></div>
    <div class="side-box" style="top:137px;height:72px;border:0"><h3 class="side-title" style="top:14px">Customer Service</h3><div class="contact-link" style="top:37px">Contact</div></div>
    <div class="promo" style="top:209px;width:144px;height:94px"><h3>Lorem</h3><p>Lorem Ipsum any text can go here.<br>Or. This can go all-together.</p></div>
    <div class="pay-badge"></div>
  </aside>

  <footer class="abs footer-links">
    <div class="footer-col"><h4>New Products</h4><ul><li>Lorem</li><li>Ipsum</li><li>Lorem Ipsum</li><li>Ipsum Lorem</li></ul></div>
    <div class="footer-col"><h4>Another Title</h4><ul><li>Lorem</li><li>Ipsum</li><li>Lorem Ipsum</li><li>Ipsum Lorem</li></ul></div>
    <div class="footer-col"><h4>Another Title</h4><ul><li>Lorem</li><li>Ipsum</li><li>Lorem Ipsum</li><li>Ipsum Lorem</li></ul></div>
  </footer>

  <div class="abs bottom-bar">
    <nav class="bottom-nav">Cart (0 items) &nbsp;/&nbsp; Customer Service &nbsp;/&nbsp; Privacy Policy &nbsp;/&nbsp; Site Map &nbsp;/&nbsp; Search Terms &nbsp;/&nbsp; Advanced Search &nbsp;/&nbsp; Contact Us &nbsp;/</nav>
    <div class="to-top"><svg width="8" height="8" viewBox="0 0 8 8"><path d="M1 5.5L4 2.5 7 5.5" fill="none" stroke="#fff" stroke-width="1.4"/></svg></div>
  </div>

</div>
</body>
</html>
```